Tequila Bottle Labels

We are a construction company that bottled our own tequila and would like a unique label for it! We already have our own company logo (linked below) and we want that logo somewhere on the bottle as well- it can be big or small. It was brewed & bottled in Southern California. Ideally it would have the year "2020," "Single Estate," & "100% Agave Azul" somewhere on the label.

Tequila / RMT / 2020

```html
<!DOCTYPE html>
<html lang="en">
<head>
<meta charset="utf-8">
<title>RMT Tequila Label</title>
<link rel="stylesheet" href="https://fonts.googleapis.com/css2?family=Cormorant+SC:wght@500&family=Open+Sans:wght@400&family=Arimo:wght@400;700&display=swap">
<style>
  :root {
    --paper: #ffffff;
    --navy: #1f3f78;
    --gold: #9a7d34;
    --gold-soft: #c9b27a;
    --ink: #23417a;
  }
  html, body {
    margin: 0;
    padding: 0;
    overflow: hidden;
    background: var(--paper);
  }
  .label {
    position: relative;
    width: 1200px;
    height: 1195px;
    background: var(--paper);
  }
  .label > * {
    position: absolute;
    left: 0;
    width: 100%;
    margin: 0;
    text-align: center;
    line-height: 1;
  }
  .agave-emblem {
    top: 300px;
    left: 500px;
    width: 200px;
    height: 90px;
    border-radius: 100px 100px 8px 8px;
    background: linear-gradient(180deg, var(--gold-soft), var(--gold));
  }
  .brand-name {
    top: 440px;
    font-family: "Open Sans", Arial, sans-serif;
    font-weight: 400;
    font-size: 150px;
    letter-spacing: 6px;
    color: var(--navy);
  }
  .vintage {
    top: 612px;
    font-family: "Arimo", Arial, sans-serif;
    font-weight: 700;
    font-size: 30px;
    letter-spacing: 10px;
    color: var(--navy);
  }
  .product-name {
    top: 660px;
    font-family: "Cormorant SC", Georgia, serif;
    font-weight: 500;
    font-size: 64px;
    letter-spacing: 3px;
    color: var(--gold);
  }
  .agave-note {
    top: 740px;
    font-family: "Open Sans", Arial, sans-serif;
    font-size: 33px;
    color: var(--ink);
  }
  .strength {
    top: 818px;
    font-family: "Arimo", Arial, sans-serif;
    font-size: 21px;
    color: var(--ink);
  }
  .volume {
    top: 860px;
    font-family: "Arimo", Arial, sans-serif;
    font-weight: 700;
    font-size: 26px;
    color: var(--ink);
  }
</style>
</head>
<body>
  <main class="label">
    <div class="agave-emblem" role="img" aria-label="Gold agave emblem"></div>
    <p class="brand-name">RMT</p>
    <p class="vintage">2020</p>
    <h1 class="product-name">Tequila</h1>
    <p class="agave-note">100% agave azul</p>
    <p class="strength">40% alcohol</p>
    <p class="volume">750ml</p>
  </main>
</body>
</html>
```